Launch of a new Investment fund

Im looking for someone design a logo and website for my Investment fund located in Singapore.

Attached to this project you will find a project scope document that details exactly what i am looking for and also includes a website copy that i have written up. I am happy for you to take your own inspiration as well to design the website. At this stage the website wont be very detailed as there isn't much information to showcase. I will require the website to be easily editable in the future so i can update it with progress the fund makes.

If you require any further details on the project please reach out to me

Coding

Coded - Design and coding required

Number of Pages Required

4 page

```html
<!DOCTYPE html>
<html lang="en">
<head>
<meta charset="utf-8">
<title>Norvale Capital Management</title>
<link rel="stylesheet" href="https://fonts.googleapis.com/css2?family=Montserrat:wght@400;500;600;700;800&display=swap">
<style>
:root{
  --navy:#0c1f5e;
  --cyan:#1aa6da;
  --ink:#3a3f4a;
  --dark:#1d1d1d;
  --team-bg:#1d1b19;
  --invest-bg:#0b2a52;
  --invest-line:#9fb4cc;
  --soft-bg:#e6f3fb;
  --footer-bg:#0c1f66;
  --form-bg:#e9ecf0;
  --white:#ffffff;
}
*{box-sizing:border-box;margin:0;padding:0}
html,body{width:1200px;height:4254px;overflow:hidden}
body{font-family:"Montserrat",sans-serif;color:var(--ink);background:var(--white);position:relative}
section,header,footer{position:absolute;left:0;width:1200px;overflow:hidden}
.abs{position:absolute}

/* header */
.site-header{top:0;height:85px;background:var(--white)}
.brand{display:flex;align-items:center;gap:12px}
.brand-mark{width:56px;height:56px;background:var(--cyan)}
.brand-name{font-weight:700;color:var(--navy);font-size:20px;line-height:29px}
.site-header .brand{left:97px;top:15px}
.main-nav{right:100px;top:32px;display:flex;gap:34px;font-size:15px;color:#333}
.main-nav .active{color:var(--navy);font-weight:700}

/* hero */
.hero{top:85px;height:600px;background:linear-gradient(115deg,#0d3a5c 0%,#145479 45%,#2d6687 70%,#7a8c99 100%)}
.hero-photo{inset:0}
.hero-title{left:97px;top:143px;font-weight:800;font-size:49px;line-height:68px;color:var(--white);letter-spacing:1px}
.hero-title span{color:var(--cyan)}
.play-btn{left:97px;top:378px;width:64px;height:64px;border-radius:50%;background:#fff;border:6px solid #a9c2d4;display:flex;align-items:center;justify-content:center}

/* about */
.about{top:685px;height:635px;background:var(--white)}
.about-back{left:99px;top:101px;width:403px;height:422px;background:#dfe3ea;border-radius:14px}
.about-photo{left:132px;top:138px;width:434px;height:349px;border-radius:14px;background:radial-gradient(circle at 55% 55%,#4a6f86 0%,#1e3446 45%,#0f1c27 100%)}
.section-title{font-weight:800;color:var(--navy);font-size:32px;letter-spacing:.5px}
.about .section-title{left:647px;top:97px}
.about-copy{left:647px;top:150px;width:450px;font-size:15px;line-height:31px;color:#3b3b3b}
.about-copy p+p{margin-top:31px}

/* team */
.team{top:1320px;height:614px;background:var(--team-bg)}
.team-title{left:96px;top:108px;font-weight:700;font-size:28px;color:var(--white)}
.team-sub{left:100px;top:163px;font-size:21px;font-weight:500;color:var(--white)}
.team-copy{left:100px;top:207px;width:480px;font-size:15px;line-height:31px;color:#e8e8e8}
.team-copy p+p{margin-top:31px}
.team-back{left:695px;top:100px;width:411px;height:416px;background:#464545;border-radius:14px}
.team-photo{left:650px;top:137px;width:428px;height:340px;border-radius:14px;background:linear-gradient(120deg,#8a6f66 0%,#5a4a4a 40%,#2f3a4f 70%,#1f2330 100%)}
.team-dot{left:1020px;top:418px;width:46px;height:46px;border-radius:50%;background:var(--cyan)}

/* investments */
.investments{top:1934px;height:752px;background:var(--invest-bg)}
.investments .heading{left:0;width:1200px;top:80px;text-align:center;font-weight:800;font-size:30px;color:var(--white)}
.investments .lead{left:0;width:1200px;top:148px;text-align:center;font-size:16px;line-height:34px;color:var(--white);font-weight:500}
.diagram{left:0;top:0}
.pillar h3{font-size:17px;font-weight:700;color:var(--white);margin-bottom:14px}
.pillar p{font-size:16.5px;line-height:35px;color:var(--white);font-weight:500}
.pillar.left{text-align:right;width:340px}
.pillar.right{width:360px}

/* companies */
.companies{top:2686px;height:488px;background:var(--soft-bg)}
.companies .section-title{left:0;width:1200px;top:86px;text-align:center;font-size:38px}
.title-rule{left:494px;top:137px;width:213px;height:3px;background:var(--cyan)}
.company-row{left:97px;top:222px;width:1010px;display:flex;justify-content:space-between;align-items:center}
.company{font-size:30px;font-weight:600;color:var(--dark)}
.carousel-dots{left:558px;top:359px;display:flex;gap:10px;align-items:center}
.carousel-dots span{width:13px;height:13px;border-radius:50%;border:1.5px solid #555}
.carousel-dots .on{width:18px;height:18px;background:var(--cyan);border-color:#0c5a85}

/* contact */
.contact{top:3174px;height:682px;background:linear-gradient(90deg,#0a2452 0%,#0d2f5e 60%,#123a6a 100%)}
.contact-title{left:87px;top:176px;font-weight:800;font-size:40px;color:var(--white)}
.contact-rule{left:87px;top:226px;width:215px;height:3px;background:var(--cyan)}
.contact-intro{left:87px;top:248px;width:470px;font-size:15px;line-height:24px;color:var(--white)}
.info{display:flex;gap:12px;color:var(--white)}
.info .label{font-size:15px;color:#d6deea}
.info .value{font-size:16px;line-height:25px}
.socials{display:flex;gap:14px;margin-top:8px}
.socials i{display:block;width:16px;height:16px;border-radius:50%;background:var(--white)}
.contact-form{left:599px;top:88px;width:543px;height:509px;background:var(--form-bg)}
.field-label{font-size:13px;color:#222;font-weight:500}
.field{background:#eef0f3;border:1px solid #a6abb3;border-radius:2px;font-size:12px;color:#8b9099;padding:0 18px;display:flex;align-items:center}
.send-btn{left:30px;top:438px;width:483px;height:46px;background:linear-gradient(180deg,#28b6e6,#0b89c2);color:var(--white);font-weight:700;font-size:14px;display:flex;align-items:center;justify-content:center}

/* footer */
.site-footer{top:3856px;height:398px;background:var(--footer-bg)}
.site-footer .brand{left:97px;top:95px}
.site-footer .brand-mark{width:80px;height:58px;background:var(--white)}
.site-footer .brand-name{color:var(--white);font-size:30px;line-height:36px;font-weight:600}
.footer-links{left:882px;top:83px;font-size:17px;line-height:33px;color:var(--white)}
.footer-rule{left:97px;width:1003px;height:1px;background:#6f7fb0}
.legal{left:97px;top:312px;display:flex;gap:14px;font-size:15px;color:var(--white)}
.copyright{left:498px;top:312px;font-size:15px;color:var(--white)}
.footer-social{left:850px;top:305px;display:flex;gap:24px}
.footer-social i{display:block;width:32px;height:32px;border-radius:50%;border:2px solid var(--white)}
</style>
</head>
<body>

<header class="site-header">
  <div class="brand abs"><div class="brand-mark"></div><div class="brand-name">Norvale<br>Capital Management</div></div>
  <nav class="main-nav abs"><span class="active">Home</span><span>What we Do</span><span>Our Team</span><span>Investments</span><span>Contact Us</span></nav>
</header>

<section class="hero">
  <div class="hero-photo abs" role="img" aria-label="Aerial view of a container ship crossing deep blue ocean"></div>
  <h1 class="hero-title abs"><span>PASSION</span> FOR<br>UNCOVERING NEW<br>OPPORTUNITIES</h1>
  <div class="play-btn abs"><svg width="20" height="22" viewBox="0 0 20 22"><path d="M3 2 L18 11 L3 20 Z" fill="#0c1f5e"/></svg></div>
</section>

<section class="about">
  <div class="about-back abs"></div>
  <div class="about-photo abs" role="img" aria-label="Hand holding a glowing rising bar chart with an upward arrow"></div>
  <h2 class="section-title abs">WHAT WE DO (ABOUT US)</h2>
  <div class="about-copy abs">
    <p>A beacon of innovative investment where strategic diversification meets meticulous market comprehension. We navigate the complexities of Global Equities, Real Estate, Venture Capital, Private Equity, and Alternative Assets, focusing on uncovering distinctive investment opportunities for our investors.</p>
    <p>At Norvale, investment is not just a transaction; it's a carefully orchestrated process, mirroring the meticulous management of personal assets. Our ethos is built on a bedrock of expansive market wisdom and proactive strategy formulation, ensuring our portfolio remains both robust and agile.</p>
  </div>
</section>

<section class="team">
  <h2 class="team-title abs">OUR TEAM (MEET OUR FOUNDER)</h2>
  <div class="team-sub abs">The Architect of Norvale's Visionary Path</div>
  <div class="team-copy abs">
    <p>Meet Ravi, the driving force behind Norvale Capital Management. From co-founding the region's second-largest renewable energy company to pioneering ventures in diverse sectors, Ravi's entrepreneurial journey is marked by a passion for market innovation and sustainable growth.</p>
    <p>With over a decade of diverse business scaling experience, Ravi established Norvale Capital, evolving from personal investment to a trust-fortified endeavour of market innovation and niche investment exploration.</p>
  </div>
  <div class="team-back abs"></div>
  <div class="team-photo abs" role="img" aria-label="Portrait of the founder in a suit and tie"></div>
  <div class="team-dot abs"></div>
</section>

<section class="investments">
  <h2 class="heading abs">INVESTMENTS</h2>
  <p class="lead abs">Norvale's portfolio showcases our ability to identify undervalued opportunities with<br>significant growth potential.</p>
  <svg class="diagram abs" width="1200" height="752" viewBox="0 0 1200 752">
    <g fill="none" stroke="var(--invest-line)" stroke-width="1.5">
      <path d="M550 307 H574 V576"/>
      <path d="M550 446 H560 V576"/>
      <path d="M655 307 H612 V576"/>
      <path d="M655 446 H626 V576"/>
    </g>
    <g fill="#ffffff"><circle cx="550" cy="307" r="4"/><circle cx="550" cy="446" r="4"/><circle cx="655" cy="307" r="4"/><circle cx="655" cy="446" r="4"/></g>
    <g stroke="#6d8aad" stroke-width="3" fill="#0a2140">
      <path d="M512 270 L544 288 V326 L512 344 L480 326 V288 Z"/>
      <path d="M693 270 L725 288 V326 L693 344 L661 326 V288 Z"/>
      <path d="M512 409 L544 427 V465 L512 483 L480 465 V427 Z"/>
      <path d="M693 409 L725 427 V465 L693 483 L661 465 V427 Z"/>
    </g>
    <g fill="none" stroke="#fff" stroke-width="1.8">
      <rect x="496" y="305" width="5" height="14"/><rect x="505" y="300" width="5" height="19"/><rect x="514" y="295" width="5" height="24"/><rect x="523" y="290" width="5" height="29"/>
      <circle cx="680" cy="298" r="8"/><rect x="690" y="304" width="5" height="15"/><rect x="699" y="298" width="5" height="21"/>
      <path d="M498 468 V448 L512 436 L526 448 V468 Z"/><rect x="507" y="456" width="10" height="12"/>
      <circle cx="685" cy="440" r="7"/><path d="M672 470 Q685 452 698 470"/><circle cx="706" cy="458" r="9"/>
    </g>
    <rect x="550" y="578" width="100" height="72" fill="var(--cyan)"/>
    <rect x="558" y="586" width="84" height="56" fill="none" stroke="#fff" stroke-width="2"/>
  </svg>
  <div class="pillar left abs" style="left:92px;top:254px"><h3>GLOBAL EQUITY MARKETS</h3><p>We've demonstrated exceptional skill<br>in identifying undervalued stocks and</p></div>
  <div class="pillar right abs" style="left:761px;top:259px"><h3>VENTURE CAPITAL</h3><p>Strategic investments in venture<br>capital, where we harness our industry</p></div>
  <div class="pillar left abs" style="left:92px;top:393px"><h3>PROPERTY DEVELOPMENT</h3><p>Curated development projects,<br>exemplifying our ability to identify</p></div>
  <div class="pillar right abs" style="left:761px;top:393px"><h3>PRIVATE EQUITY</h3><p>Access to investments in cutting edge<br>sectors, featuring companies like</p></div>
</section>

<section class="companies">
  <h2 class="section-title abs">COMPANIES WE HAVE ACCESS TO INVESTING</h2>
  <div class="title-rule abs"></div>
  <div class="company-row abs">
    <div class="company">Lumora AI</div>
    <div class="company">Chatterly</div>
    <div class="company">Pixelwave</div>
    <div class="company">Datavault</div>
    <div class="company">Orbitra</div>
  </div>
  <div class="carousel-dots abs"><span></span><span></span><span></span><span class="on"></span></div>
</section>

<section class="contact">
  <h2 class="contact-title abs">CONTACT US</h2>
  <div class="contact-rule abs"></div>
  <p class="contact-intro abs">Join us on this journey toward financial freedom. Let Norvale Capital Management be your guide. Illuminating the path to a brighter, more secure future.</p>
  <div class="info abs" style="left:90px;top:361px">
    <svg width="22" height="22" viewBox="0 0 22 22"><rect x="1" y="4" width="20" height="14" fill="var(--cyan)"/><path d="M1 4 L11 12 L21 4" stroke="#0b2450" stroke-width="1.6" fill="none"/></svg>
    <div><div class="label">Email</div><div class="value">hello@norvalecapital.com</div></div>
  </div>
  <div class="info abs" style="left:370px;top:361px">
    <svg width="22" height="22" viewBox="0 0 22 22"><path d="M4 2 L8 2 L10 7 L7.5 9 Q10 14 13 15 L15 12.5 L20 14.5 L20 18 Q19 21 15 20 Q5 17 2 6 Q2 2 4 2 Z" fill="var(--cyan)"/></svg>
    <div><div class="label">Call Us</div><div class="value">+1 (555) 014-2290</div></div>
  </div>
  <div class="info abs" style="left:90px;top:456px">
    <svg width="22" height="26" viewBox="0 0 22 26"><path d="M11 1 C5 1 2 5 2 10 C2 16 11 25 11 25 C11 25 20 16 20 10 C20 5 17 1 11 1 Z" fill="var(--cyan)"/><circle cx="11" cy="10" r="3.5" fill="#0b2450"/></svg>
    <div><div class="label">Address</div><div class="value">42 Harbour Lane, Westfield<br>Ontario, Canada, 10293</div></div>
  </div>
  <div class="info abs" style="left:365px;top:463px">
    <svg width="28" height="28" viewBox="0 0 28 28"><circle cx="8" cy="8" r="5" fill="var(--cyan)"/><circle cx="20" cy="8" r="5" fill="var(--cyan)"/><circle cx="8" cy="20" r="5" fill="var(--cyan)"/><circle cx="20" cy="20" r="5" fill="var(--cyan)"/></svg>
    <div><div class="label">Social</div><div class="socials"><i></i><i></i><i></i><i></i></div></div>
  </div>

  <form class="contact-form abs">
    <div class="field-label abs" style="left:30px;top:30px">First Name</div>
    <div class="field abs" style="left:30px;top:49px;width:234px;height:42px">First Name</div>
    <div class="field-label abs" style="left:279px;top:30px">Last Name</div>
    <div class="field abs" style="left:279px;top:49px;width:234px;height:42px">Last Name</div>
    <div class="field-label abs" style="left:30px;top:111px">Email</div>
    <div class="field abs" style="left:30px;top:131px;width:483px;height:42px">Email</div>
    <div class="field-label abs" style="left:28px;top:192px">Phone Number</div>
    <div class="field abs" style="left:30px;top:211px;width:483px;height:42px">Phone Number</div>
    <div class="field-label abs" style="left:28px;top:274px">Message</div>
    <div class="field abs" style="left:30px;top:291px;width:483px;height:132px"></div>
    <div class="send-btn abs">SEND MESSAGE</div>
  </form>
</section>

<footer class="site-footer">
  <div class="brand abs"><div class="brand-mark"></div><div class="brand-name">Norvale<br>Capital Management</div></div>
  <div class="footer-links abs">Our Teams<br>What We Do<br>Careers<br>News &amp; Insights</div>
  <div class="footer-rule abs" style="top:286px"></div>
  <div class="legal abs"><span>Privacy</span><span>Terms of Use</span><span>Notices</span><span>Disclosures</span></div>
  <div class="copyright abs">©2024.Norvale Capital.All Rights Reserved</div>
  <div class="footer-social abs"><i></i><i></i><i></i><i></i><i></i></div>
  <div class="footer-rule abs" style="top:366px"></div>
</footer>

</body>
</html>
```